Tease by Dusk Age Verification Landing Page

To create a visually appealing design for the landing page of the adult game "Tease by Dusk" that confirms the visitor's age.
The design should have a simple and visually appealing look that focuses on two buttons labeled "Yes" and "No". The purpose of the page is to confirm that the visitor is 18 years of age or older before accessing the game's content. Responsive design that works well on desktop and mobile devices. The final output should be delivered in PSD, AI, or Sketch format, along with any necessary images or assets.
I have also attached examples.

```html
<!DOCTYPE html>
<html lang="en">
<head>
<meta charset="utf-8">
<title>Tease by Dusk — Age Verification</title>
<link href="https://fonts.googleapis.com/css2?family=Syne:wght@400;500&display=swap" rel="stylesheet">
<style>
  :root {
    --page-black: #050205;
    --curtain-crimson: #8a0c3a;
    --curtain-magenta: #6a1257;
    --curtain-plum: #3a0a36;
    --text-white: #ffffff;
    --brand-mauve: #c690c8;
    --button-yes: #7d4e99;
    --button-no: #b3102f;
    --check-red: #c8102e;
  }
  * { box-sizing: border-box; margin: 0; padding: 0; }
  html, body {
    width: 1200px;
    height: 800px;
    overflow: hidden;
    background: var(--page-black);
    font-family: "Syne", "Helvetica Neue", Arial, sans-serif;
  }
  .age-gate {
    position: relative;
    width: 1200px;
    height: 800px;
    background: var(--page-black);
  }
  .hero-scene {
    position: absolute;
    left: 290px;
    top: 0;
    width: 640px;
    height: 660px;
    background:
      radial-gradient(ellipse 42% 55% at 50% 40%, rgba(20,2,14,0.75), rgba(20,2,14,0) 70%),
      linear-gradient(90deg, var(--curtain-crimson) 0%, #7a0d42 35%, var(--curtain-magenta) 65%, var(--curtain-plum) 100%);
    -webkit-mask-image: linear-gradient(180deg, #000 0%, #000 45%, transparent 100%);
    mask-image: linear-gradient(180deg, #000 0%, #000 45%, transparent 100%);
  }
  .gate-content {
    position: absolute;
    left: 0;
    top: 0;
    width: 1200px;
    display: flex;
    flex-direction: column;
    align-items: center;
  }
  .brand {
    margin-top: 180px;
    display: flex;
    align-items: center;
    gap: 10px;
  }
  .brand-dot {
    width: 14px;
    height: 14px;
    border-radius: 50%;
    background: var(--text-white);
  }
  .brand-name {
    font-size: 22px;
    font-weight: 400;
    color: var(--brand-mauve);
    letter-spacing: 0.5px;
  }
  .age-question {
    margin-top: 64px;
    font-size: 23px;
    font-weight: 400;
    line-height: 34px;
    color: var(--text-white);
    text-align: center;
    letter-spacing: 0.8px;
  }
  .answer-buttons {
    margin-top: 22px;
    display: flex;
    gap: 20px;
  }
  .answer-button {
    width: 125px;
    height: 37px;
    border: none;
    border-radius: 19px;
    font-family: inherit;
    font-size: 18px;
    color: var(--text-white);
    cursor: pointer;
  }
  .answer-button--yes { background: var(--button-yes); }
  .answer-button--no { background: var(--button-no); }
  .remember-me {
    margin-top: 22px;
    display: flex;
    align-items: center;
    gap: 7px;
    font-size: 11px;
    font-weight: 500;
    color: var(--text-white);
  }
  .remember-box {
    width: 13px;
    height: 13px;
    border-radius: 2px;
    background: var(--text-white);
    display: flex;
    align-items: center;
    justify-content: center;
  }
  .remember-box span {
    width: 7px;
    height: 7px;
    border-radius: 50%;
    background: var(--check-red);
  }
</style>
</head>
<body>
  <main class="age-gate">
    <div class="hero-scene" role="img" aria-label="Silhouette of a couple embracing in front of a red velvet curtain"></div>
    <section class="gate-content">
      <div class="brand">
        <span class="brand-dot"></span>
        <span class="brand-name">Tease by Dusk</span>
      </div>
      <h1 class="age-question">Are you<br>over 18 years of age?</h1>
      <div class="answer-buttons">
        <button class="answer-button answer-button--yes">Yes</button>
        <button class="answer-button answer-button--no">No</button>
      </div>
      <label class="remember-me">
        <span class="remember-box"><span></span></span>
        Remember me
      </label>
    </section>
  </main>
</body>
</html>
```